Home page in PSD needed for a Business Consultant website

We have been given the mandate to re-do the website: http://www.lumivanconseil.ca/

Deliverable: home page in PSD format in French language

Context: Luc Dorval is a business strategist specializing in marketing, creativity, business development. He helps small and medium companies develop their business through creative marketing strategies.

Some websites we like for your inspiration:

http://www.tallpinegrove.com.au/
http://www.trwadvisory.com.au/
http://fjalladvisors.com.au/
http://www.olubrenix.com/fr

Target Market(s)

B2B: Companies looking on the web for a business consultant who can help them with marketing, business developement, printing needs.

Industry/Entity Type

Business

Requirements
Must have
• Call to action: "Simplifiez votre développement des affaires" (which means "Simplify your business development")
• List of services (main menu)
• Marketing
• Développement des affaires
• Créativité
• Scolaire
• Impression
• Top menu as follow:
• Accueil
• À propos
• Contact

```html
<!DOCTYPE html>
<html lang="fr">
<head>
<meta charset="utf-8">
<title>Lumivan Conseil</title>
<link rel="stylesheet" href="https://fonts.googleapis.com/css2?family=Arimo:wght@400;700&family=Noto+Serif:wght@400;700&display=swap">
<style>
:root{
  --blue:#0b78c4;
  --blue-dark:#0667ad;
  --charcoal:#333333;
  --nav-active:#5c5c5c;
  --text:#555555;
  --card-bg:#f7f7f7;
  --card-line:#e4e4e4;
  --white:#ffffff;
}
*{margin:0;padding:0;box-sizing:border-box}
html,body{width:1149px;height:1200px;overflow:hidden;background:var(--white)}
body{position:relative;font-family:"Arimo",Arial,sans-serif;color:var(--text)}
.abs{position:absolute}

/* header */
.header-shape{left:0;top:0;width:1149px;height:99px}
.brand{left:150px;top:20px;width:270px}
.brand-name{font-family:"Noto Serif",Georgia,serif;font-size:27px;color:#222;display:flex;align-items:center;gap:8px;white-space:nowrap}
.brand-name .dot{width:12px;height:12px;border-radius:50%;background:var(--blue);display:inline-block}
.brand-tag{font-size:8.5px;letter-spacing:1.6px;color:#555;margin-top:8px;padding-left:26px}
.top-menu{left:560px;top:24px;display:flex;gap:22px;list-style:none}
.top-menu a{color:var(--white);text-decoration:none;font-size:12px}
.call{left:840px;top:13px;display:flex;gap:12px;align-items:center}
.call-icon{width:33px;height:33px;background:#d7e9f7;border-radius:6px;display:flex;align-items:center;justify-content:center}
.call-text{color:var(--white);font-weight:700;font-size:17.5px;line-height:17px}
.nav{left:480px;top:63px;display:flex;height:36px}
.nav a{color:var(--white);text-decoration:none;font-size:12.5px;line-height:36px;padding:0 17px;white-space:nowrap}
.nav a.active{background:var(--nav-active)}

/* hero */
.hero{left:144px;top:135px;width:862px;height:311px;background:linear-gradient(90deg,#2a2a2c 0%,#4a4a4e 45%,#3a3a3d 75%,#1e1e20 100%)}
.cta{left:560px;top:215px;width:420px}
.cta-title{font-family:"Noto Serif",Georgia,serif;font-size:30px;line-height:38px;color:var(--white);font-weight:400}
.cta-btn{display:inline-block;margin-top:22px;background:var(--blue);color:var(--white);font-size:13px;padding:10px 22px;text-decoration:none}

/* about */
.portrait{left:144px;top:479px;width:153px;height:177px;border:1px solid #d5d5d5;background:linear-gradient(180deg,#f2f2f2 0%,#e6e6e6 55%,#3b3d45 100%)}
.about-title{left:323px;top:478px;font-family:"Noto Serif",Georgia,serif;font-size:25px;color:#111;font-weight:400}
.about-title span{color:var(--blue)}
.about-text{left:321px;top:527px;width:685px;font-size:11.6px;line-height:16.2px;text-align:justify;letter-spacing:.15px}
.about-text p+p{margin-top:15px}
.divider{left:160px;top:696px;width:830px;height:4px;background:radial-gradient(ellipse at center,rgba(0,0,0,.12) 0%,rgba(0,0,0,0) 70%)}

/* service cards */
.card{top:743px;width:252px;height:243px;background:var(--card-bg);border:1px solid var(--card-line);overflow:hidden}
.card-img{height:114px}
.card-title{font-family:"Noto Serif",Georgia,serif;font-size:15px;color:var(--blue);margin:13px 11px 0;line-height:16px}
.card-title b{font-weight:700}
.card-text{font-size:10.4px;line-height:14.4px;margin:6px 11px 0;text-align:justify;letter-spacing:.4px}
.card-more{position:absolute;right:0;bottom:0;width:110px;height:22px}
.card-more span{position:absolute;right:10px;top:4px;color:var(--white);font-size:11px}

/* footer */
.footer-shape{left:0;top:1041px;width:1149px;height:159px}
.f-col{top:1053px;color:var(--white)}
.f-col h3{font-weight:400;font-size:14.5px;margin-bottom:10px}
.f-list{list-style:none;font-size:11px;line-height:19.8px;color:#e6e6e6;letter-spacing:.4px}
.f-row{display:flex;gap:10px;font-size:10.5px;line-height:12.5px;color:#e6e6e6;margin-bottom:12px;letter-spacing:.3px}
.f-row b{color:var(--white)}
.f-sq{width:20px;height:20px;background:#8a8a8a;flex:none}
.f-brand{left:754px;top:1092px;color:var(--white)}
.f-brand .brand-name{color:var(--white)}
.f-brand .brand-name .dot{background:var(--white)}
.f-brand .brand-tag{color:#e3effa}
.copy{left:770px;top:1167px;color:var(--white);font-size:10.5px}
</style>
</head>
<body>

<svg class="abs header-shape" viewBox="0 0 1149 99" aria-hidden="true">
  <rect width="1149" height="99" fill="#0b78c4"/>
  <rect x="420" y="63" width="729" height="36" fill="#333"/>
  <polygon points="157,0 494,0 427,99 90,99" fill="#fff"/>
</svg>

<div class="abs brand">
  <div class="brand-name"><span class="dot"></span>LUMIVAN Conseil</div>
  <div class="brand-tag">commercialisation | marketing | créativité</div>
</div>

<ul class="abs top-menu">
  <li><a href="#">Accueil</a></li>
  <li><a href="#">À propos</a></li>
  <li><a href="#">Contact</a></li>
</ul>

<div class="abs call">
  <div class="call-icon">
    <svg width="18" height="20" viewBox="0 0 18 20"><path d="M4 1 L7 1 L8 6 L5.5 7.5 C6.5 11 8 13 11 14.5 L12.5 12 L17 13 L17 16 C17 18 15 19 13 18.5 C7 17 2 11 1.5 5 C1.3 3 2 1 4 1Z" fill="#0b78c4"/></svg>
  </div>
  <div class="call-text">Luc Dorval<br>514 555 0182</div>
</div>

<nav class="abs nav">
  <a class="active" href="#">Marketing</a>
  <a href="#">Développement des affaires</a>
  <a href="#">Créativité</a>
  <a href="#">Scolaire</a>
  <a href="#">Impression</a>
</nav>

<div class="abs hero" role="img" aria-label="Photo d'un homme en costume dessinant un schéma de stratégie d'affaires à la craie sur fond sombre"></div>
<div class="abs cta">
  <h2 class="cta-title">Simplifiez votre développement des affaires</h2>
  <a class="cta-btn" href="#">Contactez-moi</a>
</div>

<div class="abs portrait" role="img" aria-label="Portrait de Luc Dorval en veston"></div>
<h1 class="abs about-title">À propos de <span>LUC DORVAL</span></h1>
<div class="abs about-text">
  <p>Lorem ipsum dolor sit amet, consectetur adipiscing elit. Sed placerat mauris at felis vehicula faucibus ac ac dui. Maecenas in mattis lectus. Donec gravida, purus ac lobortis condimentum, tellus justo euismod sapien, imperdiet eleifend nisl tellus sit amet lorem. Pellentesque vel suscipit arcu. Proin sollicitudin vel nunc non consequat. Maecenas dolor turpis, consequat eget adipiscing nec, sagittis sed est.</p>
  <p>Lorem ipsum dolor sit amet, consectetur adipiscing elit. Sed placerat mauris at felis vehicula faucibus ac ac dui. Maecenas in mattis lectus. Donec gravida, purus ac lobortis condimentum, tellus justo euismod sapien, imperdiet eleifend nisl tellus sit amet lorem.</p>
</div>
<div class="abs divider"></div>

<div class="abs card" style="left:144px">
  <div class="card-img" role="img" aria-label="Schéma marketing dessiné sur papier avec crayon" style="background:linear-gradient(135deg,#f3ece2,#e9e3da 60%,#d8d2c8)"></div>
  <div class="card-title">Stratégie <b>MARKETING</b></div>
  <div class="card-text">Lorem ipsum dolor sit amet, consectetur adipiscing elit. Curabitur et lectus vulputate, pharetra quam id, pharetra odio. Vestibulum eget enim vel quam.</div>
  <div class="card-more"><svg width="110" height="22"><polygon points="20,0 110,0 110,22 0,22" fill="#0b78c4"/></svg><span>En savoir plus</span></div>
</div>

<div class="abs card" style="left:449px">
  <div class="card-img" role="img" aria-label="Homme d'affaires présentant des idées dessinées à la craie" style="background:linear-gradient(90deg,#3a3f48,#4d525b 50%,#3a3f48)"></div>
  <div class="card-title">Stratégie <b>CRÉATIVE</b></div>
  <div class="card-text">Lorem ipsum dolor sit amet, consectetur adipiscing elit. Curabitur et lectus vulputate, pharetra quam id, pharetra odio. Vestibulum eget enim vel quam.</div>
  <div class="card-more"><svg width="110" height="22"><polygon points="20,0 110,0 110,22 0,22" fill="#0b78c4"/></svg><span>En savoir plus</span></div>
</div>

<div class="abs card" style="left:754px">
  <div class="card-img" role="img" aria-label="Main sur une calculatrice devant des graphiques financiers" style="background:linear-gradient(160deg,#f1f4f8,#dbe4ee 60%,#b8c6d6)"></div>
  <div class="card-title"><b>DÉVELOPPEMENT</b><br>des affaires</div>
  <div class="card-text">Lorem ipsum dolor sit amet, consectetur adipiscing elit. Curabitur et lectus vulputate, pharetra quam id, pharetra odio.</div>
  <div class="card-more"><svg width="110" height="22"><polygon points="20,0 110,0 110,22 0,22" fill="#0b78c4"/></svg><span>En savoir plus</span></div>
</div>

<svg class="abs footer-shape" viewBox="0 0 1149 159" aria-hidden="true">
  <rect width="1149" height="159" fill="#333"/>
  <polygon points="750,0 1149,0 1149,159 644,159" fill="#0b78c4"/>
  <polygon points="745,0 750,0 647,159 642,159" fill="#fff"/>
</svg>

<div class="abs f-col" style="left:145px">
  <h3>Navigation</h3>
  <ul class="f-list"><li>Accueil</li><li>À propos</li><li>Services</li><li>Témoignages</li><li>Contact</li></ul>
</div>

<div class="abs f-col" style="left:310px">
  <h3>Nous joindre</h3>
  <div class="f-row">
    <svg width="13" height="13" viewBox="0 0 13 13" style="flex:none"><path d="M6.5 1 L12.5 6.5 L10.5 6.5 L10.5 12 L2.5 12 L2.5 6.5 L0.5 6.5Z" fill="#8a8a8a"/></svg>
    <span>Lorem ipsum, dolor sit amet,<br>Consectetur lectus.</span>
  </div>
  <div class="f-row" style="margin-top:6px">
    <svg width="13" height="13" viewBox="0 0 18 20" style="flex:none"><path d="M4 1 L7 1 L8 6 L5.5 7.5 C6.5 11 8 13 11 14.5 L12.5 12 L17 13 L17 16 C17 18 15 19 13 18.5 C7 17 2 11 1.5 5 C1.3 3 2 1 4 1Z" fill="#8a8a8a"/></svg>
    <span>514 555 0182</span>
  </div>
  <div class="f-row" style="margin-top:10px;padding-left:23px">info@lumivanconseil.ca</div>
</div>

<div class="abs f-col" style="left:547px">
  <h3>Suivez-moi</h3>
  <div class="f-row"><span class="f-sq"></span><span>Suivez-moi sur<br><b>Socialpage</b></span></div>
  <div class="f-row" style="margin-top:4px"><span class="f-sq"></span><span>Joignez-moi sur<br><b>Proflink</b></span></div>
</div>

<div class="abs f-brand">
  <div class="brand-name"><span class="dot"></span>LUMIVAN Conseil</div>
  <div class="brand-tag">commercialisation | marketing | créativité</div>
</div>
<div class="abs copy">© Lumivan Conseil 2013. Tous droits réservés</div>

</body>
</html>
```